The TopBites Fundraiser Brochure

We have tried a couple designers but they just took our ppt file and gave it back. This is the reason for us using this website. We are looking for something creative using the ppt file we have provided as an example. We have some other logo work we want done with a different name but looking to see what type of resulkts we get here first. Need a creative brochure for fundraising raising industry, working with elementary thru high schoolers. We would like to see designs that use "French Fry" font and "Leaky Ketchup" font where you see yellow text in the attached. See attached example. 81/2 X 11 Z-fold

Font styles to use
Sans Serif

Colors

Designer to choose colors to be used in the design.

Requirements
Must have
• TopBites Logo "French Fry" font where you see yellow text; i.e. fundraiser, step 1
• TopBites Logo "Leaky Ketchup" font where you see the red "my"
Nice to have
• Keeping with the TopBites theme

```html
<!DOCTYPE html>
<html lang="en">
<head>
<meta charset="utf-8">
<title>TopBites Fundraiser Brochure</title>
<link href="https://fonts.googleapis.com/css2?family=Montserrat:wght@600;700;800&family=Open+Sans:wght@400;600;700&family=Kalam:wght@700&display=swap" rel="stylesheet">
<style>
  :root{
    --navy:#2b2f86;
    --navy-deep:#1f2269;
    --yellow:#f6b91b;
    --red:#d8232a;
    --paper:#efeeeb;
    --paper-line:#e2e0dc;
    --ink:#4a4a4a;
    --white:#ffffff;
    --stage:#e4e4e4;
  }
  *{box-sizing:border-box;margin:0;padding:0}
  html,body{width:1200px;height:2400px;overflow:hidden;background:var(--stage)}
  body{font-family:"Open Sans",Arial,sans-serif;color:var(--ink);position:relative}
  .spread{position:absolute;left:40px;width:1120px;height:866px;background:var(--paper);box-shadow:0 10px 30px rgba(0,0,0,.18);overflow:hidden}
  .spread--outside{top:150px}
  .spread--inside{top:1300px}
  .panel{position:absolute;top:0;height:866px;width:373.33px;overflow:hidden}
  .panel--1{left:0}.panel--2{left:373.33px}.panel--3{left:746.66px}
  .panel-bg{position:absolute;inset:0;width:100%;height:100%}
  .fold{position:absolute;top:0;width:1px;height:100%;background:rgba(0,0,0,.08)}
  .photo{position:absolute}
  .photo--burger{background:radial-gradient(ellipse at 40% 55%,#c98a3c 0%,#8f4f1c 35%,#3d2414 75%,#2a1a10 100%)}
  .photo--pizza{background:radial-gradient(ellipse at 60% 50%,#e3a33b 0%,#c0531f 35%,#7d2a14 70%,#4a1a0d 100%)}
  .photo--hand{background:linear-gradient(160deg,#f0c9a5 0%,#d7a27c 60%,#b9825e 100%);border-radius:60px 60px 0 0}
  .brand{font-family:"Montserrat",Arial,sans-serif;font-weight:800;color:var(--yellow);letter-spacing:1px;display:flex;align-items:center;gap:10px}
  .brand-dot{width:18px;height:18px;border-radius:50%;background:var(--yellow)}
  .cover-brand{position:absolute;top:110px;left:0;width:100%;justify-content:center;font-size:58px}
  .cover-title{position:absolute;top:225px;width:100%;text-align:center;font-family:"Montserrat",Arial,sans-serif;font-weight:800;font-size:36px;color:var(--white);letter-spacing:1px}
  .phone{position:absolute;background:#f7f7f7;border:3px solid #d9d2c7;border-radius:30px;box-shadow:0 6px 16px rgba(0,0,0,.25)}
  .phone-screen{position:absolute;left:12px;right:12px;top:44px;bottom:44px;background:var(--white);overflow:hidden}
  .app-bar{height:24px;background:#2f8f4e;color:var(--white);font:700 10px "Open Sans",Arial,sans-serif;padding:6px 8px;letter-spacing:.5px}
  .badge-grid{display:grid;grid-template-columns:repeat(3,1fr);gap:14px;padding:16px 14px}
  .badge{aspect-ratio:1/1;border-radius:50%;background:#e9e9e9}
  .badge--red{background:#d94a3a}.badge--blue{background:#4a6fb5}.badge--orange{background:#f09a2a}.badge--brown{background:#7a4a2c}
  .ribbon{position:absolute;background:var(--navy);color:var(--white);font-size:13px;font-weight:600;line-height:1.35;text-align:center}
  .charity-grid{position:absolute;left:34px;top:320px;width:305px;display:grid;grid-template-columns:repeat(3,1fr);gap:26px 22px}
  .charity{height:62px;border-radius:8px;background:#d7d7d7}
  .charity--red{background:#e5a1a1}.charity--blue{background:#a8b8d8}.charity--green{background:#a9cfa9}.charity--gray{background:#c9c9c9}
  .pill{position:absolute;background:var(--yellow);color:var(--navy);font-family:"Montserrat",Arial,sans-serif;font-weight:700;border-radius:30px;text-align:center}
  .address{position:absolute;top:330px;width:100%;text-align:center;color:var(--white);font-size:14px;line-height:1.5}
  .agency{position:absolute;top:650px;left:40px;font-family:"Open Sans",Arial,sans-serif;color:#5a5a5a}
  .agency-name{font-size:30px;font-weight:600;line-height:1}
  .agency-sub{font-size:22px;font-weight:400}
  .agency-tag{font-size:11px;color:#8a8a8a;margin-top:2px}
  .step-label{position:absolute;font-family:"Kalam",cursive;font-weight:700;font-size:48px;line-height:1}
  .step-label--red{color:var(--red)}
  .step-label--yellow{color:var(--yellow)}
  .step-banner{position:absolute;left:20px;top:110px;width:300px;height:36px;background:var(--navy);color:var(--white);font:700 15px "Montserrat",Arial,sans-serif;padding:9px 14px;letter-spacing:.5px}
  .body-copy{position:absolute;left:30px;width:315px;font-size:13px;line-height:1.55;color:#555}
  .body-copy p+p{margin-top:12px}
  .register-note{position:absolute;left:190px;top:700px;width:165px;font-size:13px;font-weight:600;color:#444;line-height:1.4}
  .register-url{margin-top:8px;color:var(--yellow);font-weight:700;word-break:break-all;background:rgba(246,185,27,.12);padding:4px 6px;border-radius:4px}
  .app-phone-brand{text-align:center;margin-top:16px;font-size:22px;justify-content:center}
  .app-btn{height:12px;margin:8px 14px 0;border-radius:6px}
  .step-sub{position:absolute;left:36px;color:var(--white);font:700 13px "Montserrat",Arial,sans-serif;letter-spacing:.4px}
  .step-text{position:absolute;left:36px;width:300px;color:var(--white);font-size:13px;line-height:1.5}
  .screen-shot{position:absolute;left:50px;top:420px;width:270px;height:150px;background:linear-gradient(180deg,#ffffff 0%,#e8eef7 40%,#b9cbe6 100%);border:6px solid #f4f4f4;border-radius:10px}
  .question-list{position:absolute;left:30px;top:330px;width:320px;list-style:none}
  .question-list li{position:relative;padding-left:34px;color:var(--white);font-size:14px;line-height:1.45;margin-bottom:18px}
  .question-list li::before{content:"?";position:absolute;left:4px;top:-6px;font:800 28px "Montserrat",Arial,sans-serif;color:var(--red)}
</style>
</head>
<body>

<!-- Outside spread -->
<section class="spread spread--outside">
  <!-- Panel 1: charities -->
  <div class="panel panel--1">
    <div class="photo photo--burger" style="left:0;top:0;width:373px;height:200px" role="img" aria-label="Photo of a cheeseburger with fries"></div>
    <svg class="panel-bg" viewBox="0 0 373 866" preserveAspectRatio="none" aria-hidden="true">
      <path d="M0 200 Q190 150 373 185 L373 866 L0 866 Z" fill="var(--paper)"/>
      <path d="M0 200 Q190 150 373 185" fill="none" stroke="var(--yellow)" stroke-width="7"/>
    </svg>
    <div class="ribbon" style="left:40px;top:225px;width:295px;padding:10px 14px">Some of the other Charities<br>that we are proud to support</div>
    <div class="charity-grid">
      <div class="charity charity--blue"></div><div class="charity charity--red"></div><div class="charity charity--gray"></div>
      <div class="charity charity--gray"></div><div class="charity charity--blue"></div><div class="charity charity--red"></div>
      <div class="charity charity--green"></div><div class="charity charity--gray"></div><div class="charity charity--blue"></div>
    </div>
    <div class="pill" style="left:40px;top:770px;width:295px;height:44px;font-size:20px;padding-top:9px">www.topbites.org</div>
  </div>

  <!-- Panel 2: back -->
  <div class="panel panel--2">
    <div class="photo photo--burger" style="left:0;top:0;width:373px;height:200px" role="img" aria-label="Photo of fries beside the burger"></div>
    <svg class="panel-bg" viewBox="0 0 373 866" preserveAspectRatio="none" aria-hidden="true">
      <path d="M0 185 Q180 150 373 175 L373 866 L0 866 Z" fill="var(--paper)"/>
      <path d="M0 195 Q180 160 373 185 L373 560 Q200 640 0 580 Z" fill="var(--navy)"/>
      <path d="M0 195 Q180 160 373 185" fill="none" stroke="var(--yellow)" stroke-width="8"/>
      <path d="M373 560 Q200 640 0 580" fill="none" stroke="var(--yellow)" stroke-width="8"/>
    </svg>
    <div class="brand cover-brand" style="top:230px;font-size:50px">TopBites</div>
    <p class="address">4820 Meadow Ridge Rd, Suite 210, Box 52<br>Austin, Texas 78701<br>www.topbites.org</p>
    <div class="agency">
      <div class="agency-name">Harbor Nine</div>
      <div class="agency-sub">Marketing Group</div>
      <div class="agency-tag">A Premier Fundraising Company</div>
    </div>
  </div>

  <!-- Panel 3: cover -->
  <div class="panel panel--3">
    <svg class="panel-bg" viewBox="0 0 373 866" preserveAspectRatio="none" aria-hidden="true">
      <path d="M0 0 H373 V450 Q200 480 0 580 Z" fill="var(--navy)"/>
      <path d="M373 450 Q200 480 0 580" fill="none" stroke="var(--yellow)" stroke-width="8"/>
    </svg>
    <div class="brand cover-brand">TopBites</div>
    <h1 class="cover-title">MY FUNDRAISER</h1>
    <div class="photo photo--hand" style="left:150px;top:600px;width:223px;height:266px" role="img" aria-label="Hand holding a smartphone"></div>
    <div class="phone" style="left:80px;top:340px;width:215px;height:430px">
      <div class="phone-screen">
        <div class="app-bar">RESTAURANTS</div>
        <div class="badge-grid">
          <div class="badge badge--red"></div><div class="badge badge--blue"></div><div class="badge badge--orange"></div>
          <div class="badge badge--brown"></div><div class="badge badge--red"></div><div class="badge"></div>
          <div class="badge badge--blue"></div><div class="badge badge--orange"></div><div class="badge badge--brown"></div>
          <div class="badge badge--orange"></div><div class="badge"></div><div class="badge badge--red"></div>
        </div>
      </div>
    </div>
  </div>
  <div class="fold" style="left:373px"></div><div class="fold" style="left:746px"></div>
</section>

<!-- Inside spread -->
<section class="spread spread--inside">
  <!-- Panel 1: step 1 -->
  <div class="panel panel--1">
    <h2 class="step-label step-label--red" style="left:22px;top:40px">step 1</h2>
    <div class="step-banner">REGISTER TO PARTICIPATE</div>
    <div class="body-copy" style="top:170px">
      <p>If you have been involved or around fundraising with schools for any length of time, then you are probably familiar with coupon books or discount cards. Even though millions have been sold throughout the years, we continue to hear the same complaints: the coupon is in the other car or purse, or the coupon isn't good in my area. While the product was great, it just wasn't very user friendly. Thank goodness for technology!</p>
      <p>The TopBites app includes more than 80 of your favorite national and fast food restaurant chains. Each of them is making generous offers to encourage consumers to support your school or group.</p>
    </div>
    <div class="phone" style="left:30px;top:630px;width:145px;height:210px;border-radius:20px">
      <div class="phone-screen" style="top:28px;bottom:28px;left:8px;right:8px">
        <div class="brand app-phone-brand">TopBites</div>
        <div class="app-btn" style="background:#4caf50"></div>
        <div class="app-btn" style="background:#3f6fd1"></div>
        <div class="app-btn" style="background:#d84343"></div>
        <div class="app-btn" style="background:var(--yellow)"></div>
      </div>
    </div>
    <div class="register-note">Each participant must register. Simply type this Registration URL into your browser.
      <div class="register-url">https://topbites.org/register/topbites-fundraising/</div>
    </div>
  </div>

  <!-- Panels 2 + 3 share the photo band -->
  <div class="photo photo--pizza" style="left:373.33px;top:0;width:746.67px;height:300px" role="img" aria-label="Photo of a loaded pizza with a slice being lifted"></div>

  <div class="panel panel--2">
    <svg class="panel-bg" viewBox="0 0 373 866" preserveAspectRatio="none" aria-hidden="true">
      <path d="M0 300 Q190 250 373 240 L373 866 L0 866 Z" fill="var(--navy)"/>
      <path d="M0 300 Q190 250 373 240" fill="none" stroke="var(--yellow)" stroke-width="8"/>
    </svg>
    <h2 class="step-label step-label--yellow" style="left:34px;top:320px">step 2</h2>
    <p class="step-sub" style="top:378px">LET'S PIN, POST, TAG, TEXT, OR TWEET</p>
    <div class="screen-shot" role="img" aria-label="Screenshot of the fundraiser sharing page"></div>
    <h2 class="step-label step-label--yellow" style="left:34px;top:600px">step 3</h2>
    <p class="step-sub" style="top:658px">LET'S ASK FOR SOME HELP</p>
    <p class="step-text" style="top:682px">You just sent them a post. Let's call and ask for some help to support your fundraiser.</p>
    <div class="pill" style="left:24px;top:760px;width:325px;height:38px;font-size:15px;padding-top:9px">Call 15 family members and friends</div>
  </div>

  <!-- Panel 3: questions -->
  <div class="panel panel--3">
    <svg class="panel-bg" viewBox="0 0 373 866" preserveAspectRatio="none" aria-hidden="true">
      <path d="M0 240 Q190 230 373 290 L373 866 L0 866 Z" fill="var(--navy)"/>
      <path d="M0 240 Q190 230 373 290" fill="none" stroke="var(--yellow)" stroke-width="8"/>
    </svg>
    <ul class="question-list">
      <li>Are you tired of fundraisers where you, the parent, do all the work?</li>
      <li>Would you like a simplified process that doesn't require unsafe practices like door-to-door selling?</li>
      <li>Would you like to eliminate the hassle of collecting money and delivering items?</li>
      <li>Would you like a fundraising program that is 100% complete in one week?</li>
      <li>Would you agree that family, friends, and parents are tired of buying items that have no purpose or value?</li>
      <li>Do you agree that most family and friends would like to support a good cause?</li>
    </ul>
  </div>
  <div class="fold" style="left:373px"></div><div class="fold" style="left:746px"></div>
</section>

</body>
</html>
```